WEB HOSTING COMPANY WHMCS THEME

The name of the web host company is "crane ember" so i would like something professional and simple. Il let you guys chouse the colors use your imagination on this, i will need a logo and a business card design. I would also like the theme coded and installed to my whims server and last thing we need to setup the website to go live at te end i will pay extra for that. Thank you

Target Market(s)

Web Hosting Company

Contact Information for Business Card

CRANEEMBER

Logo Text

CRANEEMBER

Coding

Coded - Design and coding required

Number of Pages Required

5+ page

Font styles to use
Sans Serif

Requirements
Must have
• EMAIL PHONE NUMBER MOBILE NUMBER WEBSITE AND BUSINESS ADRESS

```html
<!DOCTYPE html>
<html lang="en">
<head>
<meta charset="utf-8">
<title>Crane Ember — Web Hosting</title>
<link href="https://fonts.googleapis.com/css2?family=Montserrat:wght@400;600;700&family=Open+Sans:wght@400;600;700&display=swap" rel="stylesheet">
<style>
:root{
  --green:#5fa919;
  --green-dark:#4f9212;
  --ink:#222426;
  --dark:#1f2123;
  --dark-2:#2b2e31;
  --text:#666a6e;
  --line:#e4e6e8;
  --light:#f4f5f6;
  --white:#ffffff;
}
*{box-sizing:border-box;margin:0;padding:0}
html,body{width:1200px;height:5389px;overflow:hidden}
body{font-family:"Open Sans",Arial,sans-serif;color:var(--text);font-size:13px;line-height:1.6;background:var(--white)}
h1,h2,h3,h4,.head{font-family:"Montserrat",Arial,sans-serif;color:var(--ink)}
.container{width:880px;margin:0 auto;position:relative}
section{position:relative;overflow:hidden}
.btn{display:inline-block;font-family:"Montserrat",Arial,sans-serif;font-weight:700;font-size:11px;text-transform:uppercase;letter-spacing:.5px;border-radius:20px;padding:10px 22px;background:var(--green);color:var(--white)}
.btn-dark{background:var(--ink)}
.section-title{text-align:center;font-size:22px;font-weight:700;text-transform:uppercase;letter-spacing:.5px}
.rule{width:60px;height:12px;margin:10px auto 14px;position:relative}
.rule::before{content:"";position:absolute;left:0;right:0;top:5px;height:2px;background:var(--green)}
.rule::after{content:"";position:absolute;left:25px;top:0;width:10px;height:10px;border:2px solid var(--green);background:var(--white);transform:rotate(45deg)}
.lead{text-align:center;width:720px;margin:0 auto;font-size:12.5px}

/* top bar */
.topbar{height:29px;background:var(--dark);color:#cfd2d4;font-size:11px}
.topbar .container{display:flex;justify-content:space-between;align-items:center;height:29px}
.topbar .contact{display:flex;gap:16px;align-items:center}
.topbar .live{background:var(--green);color:#fff;font-weight:700;padding:6px 14px;font-family:"Montserrat",sans-serif;font-size:10px}

/* nav */
.nav{height:107px;border-bottom:1px solid var(--line)}
.nav .container{display:flex;justify-content:space-between;align-items:center;height:107px}
.brand{display:flex;align-items:center;gap:8px;font-family:"Montserrat",sans-serif;font-weight:700;font-size:28px;color:var(--ink);letter-spacing:-.5px}
.brand .mark{width:14px;height:14px;border-radius:50%;background:var(--green)}
.menu{display:flex;gap:30px;font-family:"Montserrat",sans-serif;font-weight:600;font-size:12px;text-transform:uppercase;color:var(--ink)}
.menu .active{color:var(--green)}

/* hero */
.hero{height:539px;background:var(--white)}
.hero .visual{position:absolute;left:160px;top:43px;width:450px;height:360px;border-radius:6px;background:linear-gradient(180deg,#3b4046 0%,#1c1f22 70%,#e9ebed 100%)}
.hero .copy{position:absolute;left:675px;top:118px;width:340px}
.hero h1{font-size:30px;font-weight:700;text-transform:uppercase;margin-bottom:14px}
.hero p{font-size:12.5px;margin-bottom:14px}
.ticks{list-style:none}
.ticks li{display:flex;align-items:center;gap:10px;font-size:12.5px;margin-bottom:9px}
.ticks svg{flex:none}
.hero .btn{margin-top:10px}
.arrow{position:absolute;top:230px}

/* domain */
.domain{height:295px;background:var(--green);color:#e9f5dc}
.domain h2{color:#fff;font-size:24px;font-weight:700;text-transform:uppercase;position:absolute;left:160px;top:56px}
.domain .intro{position:absolute;left:160px;top:98px;width:700px;font-size:12px}
.domain .search{position:absolute;left:160px;top:166px;display:flex;align-items:center;gap:10px}
.domain .field{width:505px;height:38px;border-radius:20px;background:rgba(255,255,255,.25);display:flex;justify-content:space-between;align-items:center;padding:0 18px;color:#eef8e4;font-size:12px}
.domain .btn{padding:12px 26px}
.tlds{position:absolute;left:160px;top:230px;display:flex;gap:26px;font-size:11px;color:#fff}
.tlds span{display:flex;align-items:center;gap:6px}
.tlds i{width:10px;height:10px;border-radius:50%;background:#fff;display:inline-block}
.domain .cloud{position:absolute;left:860px;top:90px;width:180px;height:150px;border-radius:6px;background:rgba(255,255,255,.12)}

/* services */
.services{height:546px;padding-top:62px}
.service-grid{display:grid;grid-template-columns:repeat(3,1fr);margin-top:30px;border-top:1px solid var(--line)}
.service{display:flex;gap:16px;padding:26px 20px;height:170px;border-bottom:1px solid var(--line);border-right:1px solid var(--line)}
.service:nth-child(3n){border-right:0}
.service .ico{flex:none;width:40px;height:40px;border-radius:50%;background:var(--light);display:flex;align-items:center;justify-content:center}
.service.featured .ico{background:var(--green)}
.service h3{font-size:13px;font-weight:600;margin-bottom:6px}
.service p{font-size:11.5px}

/* stats */
.stats{height:191px;background:var(--dark)}
.stats .container{display:grid;grid-template-columns:repeat(4,1fr);height:191px;align-items:center;text-align:center}
.stat{color:#fff;border-right:1px solid #3a3d40}
.stat:last-child{border-right:0}
.stat .label{font-size:13px;margin-top:8px}
.stat .num{font-family:"Montserrat",sans-serif;font-weight:700;font-size:20px}

/* pricing */
.pricing{height:765px;padding-top:72px}
.plans{display:flex;gap:35px;margin-top:38px}
.plan{width:270px;height:485px;border:1px solid var(--line);border-radius:4px;text-align:center;box-shadow:0 2px 8px rgba(0,0,0,.05)}
.plan-head{height:150px;background:var(--ink);color:#fff;padding-top:28px;position:relative}
.plan.featured .plan-head{background:var(--green)}
.plan-head h3{color:#fff;font-size:17px;font-weight:700;text-transform:uppercase}
.plan-head p{font-size:11px;color:#d8dadc}
.price{position:absolute;left:90px;top:78px;width:90px;height:100px}
.price b{position:absolute;left:0;right:0;top:30px;font-family:"Montserrat",sans-serif;font-size:22px;color:#fff}
.price small{position:absolute;left:0;right:0;top:62px;font-size:9px;color:#fff}
.plan ul{list-style:none;margin-top:50px}
.plan li{font-size:11.5px;padding:9px 0;border-bottom:1px solid var(--line);margin:0 20px;color:var(--ink)}
.plan .btn{margin-top:24px;padding:8px 20px;font-size:10px}

/* testimonials */
.testimonials{height:356px;background:var(--green);color:#fff;text-align:center;padding-top:66px}
.testimonials h2{color:#fff;font-size:20px;font-weight:700;text-transform:uppercase}
.quote{width:760px;margin:26px auto 10px;font-size:12px;font-style:italic;display:flex;gap:14px;align-items:flex-start}
.quote .q{font-family:"Montserrat",sans-serif;font-size:34px;line-height:.8;font-weight:700}
.author{font-size:12px}
.author b{font-weight:700}
.avatars{display:flex;justify-content:center;gap:40px;margin-top:26px}
.avatars div{width:64px;height:64px;border-radius:50%;border:3px solid #fff;background:linear-gradient(180deg,#c9c3bb,#5a5450)}

/* features */
.features{height:578px}
.features .copy{position:absolute;left:160px;top:100px;width:470px}
.features h2{font-size:22px;font-weight:700;text-transform:uppercase;line-height:1.3}
.features .bar{width:50px;height:3px;background:var(--green);margin:10px 0 16px}
.features p{font-size:12px;margin-bottom:14px}
.features .ticks li{font-size:11.5px;margin-bottom:10px}
.features .photo{position:absolute;left:720px;top:40px;width:360px;height:538px;background:linear-gradient(180deg,#f1f2f3 0%,#c9ccd0 40%,#1d2b4a 100%)}

/* newsletter */
.newsletter{height:313px;background:linear-gradient(180deg,#151719,#23272b 60%,#181a1c);text-align:center;color:#bfc3c6;padding-top:66px}
.newsletter h2{color:#fff;font-size:22px;font-weight:700;text-transform:uppercase}
.newsletter .lead{color:#bfc3c6}
.subscribe{display:flex;justify-content:center;gap:10px;margin-top:30px}
.subscribe .field{width:390px;height:38px;border-radius:20px;background:rgba(255,255,255,.12);text-align:left;padding:9px 18px;font-size:12px;color:#9ba0a4}

/* faq */
.faq{height:567px;padding-top:70px}
.faq .illus{position:absolute;left:200px;top:240px;width:380px;height:290px;border-radius:6px;background:linear-gradient(180deg,#eef0f2,#d6dde4 60%,#bfe39a)}
.accordion{position:absolute;left:645px;top:268px;width:330px}
.acc-item{display:flex;align-items:center;gap:14px;background:var(--light);margin-bottom:6px;height:38px;font-size:12px;color:var(--ink)}
.acc-item .sign{width:38px;height:38px;background:var(--green);color:#fff;display:flex;align-items:center;justify-content:center;font-weight:700;font-size:16px}
.acc-body{background:#fff;border:1px solid var(--line);padding:14px 16px 14px 52px;font-size:11.5px;margin:-6px 0 6px}

/* cta */
.cta{height:205px;background:var(--green)}
.cta h2{position:absolute;left:160px;top:58px;color:#fff;font-size:34px;font-weight:700}
.cta p{position:absolute;left:160px;top:108px;color:#fff;font-family:"Montserrat",sans-serif;font-weight:600;font-size:17px}
.cta .btn{position:absolute;left:868px;top:76px;background:transparent;border:2px solid #fff;padding:12px 26px}

/* news */
.news{height:604px;padding-top:66px}
.posts{display:flex;gap:35px;margin-top:36px}
.post{width:270px;height:360px;border:1px solid var(--line)}
.post .img{height:160px}
.post .meta{display:flex;justify-content:space-between;font-size:10px;padding:10px 14px;border-bottom:1px solid var(--line)}
.post h3{font-size:16px;font-weight:700;padding:12px 14px 6px}
.post p{font-size:11.5px;padding:0 14px}
.post .btn{margin:14px 14px 0;padding:7px 16px;font-size:9px;border-radius:2px}

/* footer */
.footer{height:294px;background:var(--dark);color:#aeb2b5;font-size:11.5px}
.footer .cols{display:grid;grid-template-columns:220px 140px 140px 150px 230px;gap:0;padding-top:44px}
.footer .brand{color:#fff;font-size:24px}
.footer h4{color:#fff;font-size:14px;font-weight:600;margin-bottom:10px}
.footer ul{list-style:none;line-height:1.9}
.footer .about p{margin:10px 0 14px;width:190px}
.socials{display:flex;gap:6px}
.socials i{width:18px;height:18px;border-radius:50%;background:var(--green);display:block}
.footer .btn{margin-top:12px;padding:6px 14px;font-size:9px}
.legal{position:absolute;left:0;right:0;bottom:0;height:48px;border-top:1px solid #34373a}
.legal .container{text-align:center;line-height:48px;font-size:11px}
</style>
</head>
<body>

<header class="topbar">
  <div class="container">
    <span>English ▾</span>
    <div class="contact">
      <span>Phone: 555-014-2290</span>
      <span>Email: hello@craneember.com</span>
      <span class="live">LIVE CHAT</span>
    </div>
  </div>
</header>

<nav class="nav">
  <div class="container">
    <div class="brand"><span>craneember</span><span class="mark"></span></div>
    <div class="menu">
      <span class="active">Home</span><span>About</span><span>Hosting</span><span>Domains</span><span>Blog</span><span>Elements</span><span>Contact</span>
    </div>
  </div>
</nav>

<section class="hero">
  <svg class="arrow" style="left:46px" width="18" height="30" viewBox="0 0 18 30"><path d="M15 2 3 15l12 13" fill="none" stroke="#9a9ea2" stroke-width="2.5"/></svg>
  <div class="visual" role="img" aria-label="Row of black rack servers with glowing drive bays"></div>
  <div class="copy">
    <h1>Shared Hosting $ 25</h1>
    <p>Fast and steady hosting for every new site, with friendly help whenever you need it most.</p>
    <ul class="ticks">
      <li><svg width="14" height="14" viewBox="0 0 14 14"><circle cx="7" cy="7" r="6.5" fill="none" stroke="#5fa919"/><path d="m4 7 2 2 4-4" fill="none" stroke="#5fa919" stroke-width="1.5"/></svg>Free domain for the first year</li>
      <li><svg width="14" height="14" viewBox="0 0 14 14"><circle cx="7" cy="7" r="6.5" fill="none" stroke="#5fa919"/><path d="m4 7 2 2 4-4" fill="none" stroke="#5fa919" stroke-width="1.5"/></svg>Daily backups included</li>
      <li><svg width="14" height="14" viewBox="0 0 14 14"><circle cx="7" cy="7" r="6.5" fill="none" stroke="#5fa919"/><path d="m4 7 2 2 4-4" fill="none" stroke="#5fa919" stroke-width="1.5"/></svg>Free SSL certificate</li>
      <li><svg width="14" height="14" viewBox="0 0 14 14"><circle cx="7" cy="7" r="6.5" fill="none" stroke="#5fa919"/><path d="m4 7 2 2 4-4" fill="none" stroke="#5fa919" stroke-width="1.5"/></svg>Instant app installer</li>
      <li><svg width="14" height="14" viewBox="0 0 14 14"><circle cx="7" cy="7" r="6.5" fill="none" stroke="#5fa919"/><path d="m4 7 2 2 4-4" fill="none" stroke="#5fa919" stroke-width="1.5"/></svg>Unlimited email accounts</li>
    </ul>
    <span class="btn">Get Started</span>
  </div>
  <svg class="arrow" style="left:1136px" width="18" height="30" viewBox="0 0 18 30"><path d="m3 2 12 13L3 28" fill="none" stroke="#9a9ea2" stroke-width="2.5"/></svg>
</section>

<section class="domain">
  <h2>Search for your perfect domain name</h2>
  <p class="intro">Find the right address for your idea in seconds. Type a name, pick an ending and we check it for you straight away, so you can claim it before someone else does.</p>
  <div class="search">
    <div class="field"><span>Enter Domain Name...</span><span>| .com ▾</span></div>
    <span class="btn btn-dark">Search</span>
  </div>
  <div class="tlds">
    <span><i></i>.com</span><span><i></i>.net</span><span><i></i>.org</span><span><i></i>.biz</span><span><i></i>.info</span><span><i></i>.co</span><span><i></i>.eu</span>
  </div>
  <div class="cloud" role="img" aria-label="Line illustration of a cloud with a magnifying glass"></div>
</section>

<section class="services">
  <div class="container">
    <h2 class="section-title">Our Services</h2>
    <div class="rule"></div>
    <p class="lead">Everything a growing website needs, from quick shared plans to dedicated machines. Each service is set up by our team and watched over day and night so your pages stay online.</p>
    <div class="service-grid">
      <div class="service featured"><div class="ico"><svg width="18" height="18" viewBox="0 0 18 18"><path d="M5 13h9a3 3 0 0 0 0-6 4 4 0 0 0-8-1 3.5 3.5 0 0 0-1 7z" fill="#fff"/></svg></div><div><h3>Cloud Hosting</h3><p>Flexible space that grows with your traffic and never keeps you waiting for more room.</p></div></div>
      <div class="service"><div class="ico"><svg width="18" height="18" viewBox="0 0 18 18"><rect x="3" y="3" width="12" height="5" fill="none" stroke="#8a8e92"/><rect x="3" y="10" width="12" height="5" fill="none" stroke="#8a8e92"/></svg></div><div><h3>Dedicated Servers</h3><p>A whole machine set aside for you, with full control and steady power all month.</p></div></div>
      <div class="service"><div class="ico"><svg width="18" height="18" viewBox="0 0 18 18"><circle cx="9" cy="9" r="5" fill="none" stroke="#8a8e92"/><circle cx="9" cy="9" r="1.5" fill="#8a8e92"/></svg></div><div><h3>Domain Names</h3><p>Register and renew your names in one place, with simple tools to point them anywhere.</p></div></div>
      <div class="service"><div class="ico"><svg width="18" height="18" viewBox="0 0 18 18"><rect x="3" y="4" width="12" height="8" fill="none" stroke="#8a8e92"/><path d="M6 15h6" stroke="#8a8e92"/></svg></div><div><h3>Website Builder</h3><p>Drag blocks into place and publish a clean site without writing a single line of code.</p></div></div>
      <div class="service"><div class="ico"><svg width="18" height="18" viewBox="0 0 18 18"><path d="M9 3 4 5v4c0 3 2 5 5 6 3-1 5-3 5-6V5z" fill="none" stroke="#8a8e92"/></svg></div><div><h3>SSL Security</h3><p>Protect every visitor with trusted certificates installed and renewed on your behalf.</p></div></div>
      <div class="service"><div class="ico"><svg width="18" height="18" viewBox="0 0 18 18"><rect x="3" y="5" width="12" height="9" fill="none" stroke="#8a8e92"/><path d="m3 5 6 5 6-5" fill="none" stroke="#8a8e92"/></svg></div><div><h3>Business Email</h3><p>Professional inboxes on your own domain, with spam filters and plenty of storage.</p></div></div>
    </div>
  </div>
</section>

<section class="stats">
  <div class="container">
    <div class="stat"><svg width="22" height="22" viewBox="0 0 22 22"><circle cx="11" cy="7" r="4" fill="#5fa919"/><path d="M3 20a8 8 0 0 1 16 0z" fill="#5fa919"/></svg><div class="label">Happy Customers</div><div class="num">1,858</div></div>
    <div class="stat"><svg width="22" height="22" viewBox="0 0 22 22"><path d="M6 3h10v5a5 5 0 0 1-10 0z M9 15h4v3H9z M6 19h10v1H6z" fill="#5fa919"/></svg><div class="label">Awards Won</div><div class="num">1,858</div></div>
    <div class="stat"><svg width="22" height="22" viewBox="0 0 22 22"><path d="M6 16h11a4 4 0 0 0 0-8 5 5 0 0 0-10-1 4.5 4.5 0 0 0-1 9z" fill="#5fa919"/></svg><div class="label">Sites Hosted</div><div class="num">1,858</div></div>
    <div class="stat"><svg width="22" height="22" viewBox="0 0 22 22"><rect x="4" y="4" width="14" height="6" fill="#5fa919"/><rect x="4" y="12" width="14" height="6" fill="#5fa919"/></svg><div class="label">Dedicated Servers</div><div class="num">1,858</div></div>
  </div>
</section>

<section class="pricing">
  <div class="container">
    <h2 class="section-title">Pricing Tables</h2>
    <div class="rule"></div>
    <p class="lead">Clear monthly prices with no hidden fees. Start small and move up whenever your site needs more speed, storage or control over its own server.</p>
    <div class="plans">
      <div class="plan">
        <div class="plan-head"><h3>Shared Hosting</h3><p>Great value for starter sites</p>
          <svg class="price" viewBox="0 0 90 100"><polygon points="45,2 88,26 88,74 45,98 2,74 2,26" fill="#5fa919" stroke="#fff" stroke-width="3"/></svg>
          <div class="price"><b>$10.00</b><small>Per Month</small></div></div>
        <ul><li>1GB File storage</li><li>Unlimited products</li><li>24/7 Support</li><li>Discount code engine</li><li>All OS Supported</li><li>Sign Multiple Device</li></ul>
        <span class="btn btn-dark">Sign Up</span>
      </div>
      <div class="plan featured">
        <div class="plan-head"><h3>VPS Hosting</h3><p>Great value for busy sites</p>
          <svg class="price" viewBox="0 0 90 100"><polygon points="45,2 88,26 88,74 45,98 2,74 2,26" fill="#222426" stroke="#fff" stroke-width="3"/></svg>
          <div class="price"><b>$10.00</b><small>Per Month</small></div></div>
        <ul><li>1GB File storage</li><li>Unlimited products</li><li>24/7 Support</li><li>Discount code engine</li><li>All OS Supported</li><li>Sign Multiple Device</li></ul>
        <span class="btn">Sign Up</span>
      </div>
      <div class="plan">
        <div class="plan-head"><h3>Dedicated Server</h3><p>Great value for large sites</p>
          <svg class="price" viewBox="0 0 90 100"><polygon points="45,2 88,26 88,74 45,98 2,74 2,26" fill="#5fa919" stroke="#fff" stroke-width="3"/></svg>
          <div class="price"><b>$10.00</b><small>Per Month</small></div></div>
        <ul><li>1GB File storage</li><li>Unlimited products</li><li>24/7 Support</li><li>Discount code engine</li><li>All OS Supported</li><li>Sign Multiple Device</li></ul>
        <span class="btn btn-dark">Sign Up</span>
      </div>
    </div>
  </div>
</section>

<section class="testimonials">
  <h2>What people say about us</h2>
  <div class="quote"><span class="q">“</span><p>Moving our shop here was the easiest change we made all year. The pages load quickly, the support team answers within minutes, and we have not had a single outage since the switch. We now recommend them to every client who asks us for advice on where to host.</p><span class="q">”</span></div>
  <p class="author"><b>Mara Quill</b> / Shop owner</p>
  <div class="avatars">
    <div role="img" aria-label="Portrait photo of a customer"></div>
    <div role="img" aria-label="Portrait photo of a customer"></div>
    <div role="img" aria-label="Portrait photo of a customer"></div>
  </div>
</section>

<section class="features">
  <div class="copy">
    <h2>Hosting features<br>and benefits</h2>
    <div class="bar"></div>
    <p>Every plan comes with the tools you need to launch fast and stay secure, backed by people who care about your uptime as much as you do.</p>
    <ul class="ticks">
      <li><svg width="14" height="14" viewBox="0 0 14 14"><circle cx="7" cy="7" r="6.5" fill="none" stroke="#5fa919"/><path d="m4 7 2 2 4-4" fill="none" stroke="#5fa919" stroke-width="1.5"/></svg>One click installs for popular site tools</li>
      <li><svg width="14" height="14" viewBox="0 0 14 14"><circle cx="7" cy="7" r="6.5" fill="none" stroke="#5fa919"/><path d="m4 7 2 2 4-4" fill="none" stroke="#5fa919" stroke-width="1.5"/></svg>Solid state drives for quick page loads</li>
      <li><svg width="14" height="14" viewBox="0 0 14 14"><circle cx="7" cy="7" r="6.5" fill="none" stroke="#5fa919"/><path d="m4 7 2 2 4-4" fill="none" stroke="#5fa919" stroke-width="1.5"/></svg>Free site transfer handled by our team</li>
      <li><svg width="14" height="14" viewBox="0 0 14 14"><circle cx="7" cy="7" r="6.5" fill="none" stroke="#5fa919"/><path d="m4 7 2 2 4-4" fill="none" stroke="#5fa919" stroke-width="1.5"/></svg>Easy control panel for files and mail</li>
      <li><svg width="14" height="14" viewBox="0 0 14 14"><circle cx="7" cy="7" r="6.5" fill="none" stroke="#5fa919"/><path d="m4 7 2 2 4-4" fill="none" stroke="#5fa919" stroke-width="1.5"/></svg>Round the clock monitoring and alerts</li>
      <li><svg width="14" height="14" viewBox="0 0 14 14"><circle cx="7" cy="7" r="6.5" fill="none" stroke="#5fa919"/><path d="m4 7 2 2 4-4" fill="none" stroke="#5fa919" stroke-width="1.5"/></svg>Thirty day money back promise</li>
    </ul>
    <span class="btn">Get Started</span>
  </div>
  <div class="photo" role="img" aria-label="Photo of a smiling businessman in glasses holding an open laptop"></div>
</section>

<section class="newsletter">
  <h2>Subscribe to get our newsletter</h2>
  <div class="rule" style="background:transparent"></div>
  <p class="lead">Get hosting tips, product news and special offers sent to your inbox once a month. No spam, and you can leave the list at any time with one click.</p>
  <div class="subscribe"><div class="field">Email Address</div><span class="btn">Subscribe</span></div>
</section>

<section class="faq">
  <div class="container">
    <h2 class="section-title">Frequently Questions</h2>
    <div class="rule"></div>
    <p class="lead">Quick answers to the things new customers ask us most often. If you cannot find what you need here, our support team is only a message away.</p>
  </div>
  <div class="illus" role="img" aria-label="Illustration of a server rack, monitor, gears and clouds"></div>
  <div class="accordion">
    <div class="acc-item"><span class="sign">−</span>How quickly is my site set up?</div>
    <div class="acc-body">Most accounts are ready within a few minutes of payment. You will get an email with your login details and a short guide to help you start.</div>
    <div class="acc-item"><span class="sign">+</span>Can I upgrade my plan later?</div>
    <div class="acc-item"><span class="sign">+</span>Can I host my friends websites?</div>
    <div class="acc-item"><span class="sign">+</span>How often will I be billed?</div>
  </div>
</section>

<section class="cta">
  <h2>Start Building your Website Today</h2>
  <p>Launch in minutes with fast, friendly hosting</p>
  <span class="btn">Get Started Here</span>
</section>

<section class="news">
  <div class="container">
    <h2 class="section-title">Latest News</h2>
    <div class="rule"></div>
    <p class="lead">Updates from our team on new features, data centre upgrades and helpful guides to get the most from your hosting account.</p>
    <div class="posts">
      <div class="post">
        <div class="img" role="img" aria-label="Photo of hands typing on a laptop with a green tint" style="background:linear-gradient(180deg,#7fbf3f,#3f7a12)"></div>
        <div class="meta"><span>Jan 12, 2017</span><span>5 Comments</span></div>
        <h3>New faster storage</h3>
        <p>All plans now run on quicker drives at no extra cost to you.</p>
        <span class="btn">Read More</span>
      </div>
      <div class="post">
        <div class="img" role="img" aria-label="Photo of a technician working in a server room" style="background:linear-gradient(180deg,#4a5058,#1e2226)"></div>
        <div class="meta"><span>Jan 12, 2017</span><span>5 Comments</span></div>
        <h3>Data centre upgrade</h3>
        <p>Our main site gains new power and cooling for better uptime.</p>
        <span class="btn btn-dark">Read More</span>
      </div>
      <div class="post">
        <div class="img" role="img" aria-label="Photo of an engineer checking a rack of servers" style="background:linear-gradient(180deg,#d8dce0,#6d747b)"></div>
        <div class="meta"><span>Jan 12, 2017</span><span>5 Comments</span></div>
        <h3>Guide to backups</h3>
        <p>Learn how to restore any file from the last thirty days.</p>
        <span class="btn btn-dark">Read More</span>
      </div>
    </div>
  </div>
</section>

<footer class="footer">
  <div class="container cols">
    <div class="about">
      <div class="brand"><span>craneember</span><span class="mark"></span></div>
      <p>Simple, dependable web hosting for small teams and growing businesses everywhere.</p>
      <div class="socials"><i></i><i></i><i></i><i></i></div>
      <span class="btn">Sign up for newsletter</span>
    </div>
    <div><h4>Support</h4><ul><li>Product Support</li><li>Submit Ticket</li><li>Knowledgebase</li><li>Affiliates and Resellers</li><li>Network Status</li></ul></div>
    <div><h4>Hosting</h4><ul><li>Shared Hosting</li><li>Reseller Hosting</li><li>Cloud VPS</li><li>Dedicated Server</li><li>Domains</li></ul></div>
    <div><h4>Company</h4><ul><li>Home</li><li>Careers</li><li>About Us</li><li>Datacenter</li><li>Our Team</li></ul></div>
    <div><h4>Get in Touch With Us!</h4><ul><li>Postal address: PO Box 18 Harbour Lane, Westmere, 4021</li><li>Phone: 555-014-2290</li><li>hello@craneember.com</li></ul></div>
  </div>
  <div class="legal"><div class="container">© 2017 Crane Ember. All rights reserved. Terms and Conditions · Privacy Policy</div></div>
</footer>

</body>
</html>
```